London Based Property Finding Company - have logo already

We find property for private purchasers and investors in London, UK.  We work for the BUYER, whereas estate agencies/real estate companies work for the seller. We offer a much more personalised service to UK and overseas purchasers.

We would like the following:

*A double sided business card

*A letterhead

We have attached two versions of the logo. Each logo style is set on two different coloured backgrounds. Please choose one of the two designs, whichever you prefer or feel more comfortable with, and produce one in black and one in white background.

This applies to both pieces of stationery.

THE BUSINESS CARD:

We would like the company name placed on its own on one side of the card and the contact details and what we do on the other.

e.g.

SIDE 1:

BRAMWELL PROPERTY FINDERS

SIDE 2:

Owen Bramwell

t: 0208 394 2860

m: +44(0)7932 418 507

e: info@bramwellpropertyfinders.co.uk

w: bramwellpropertyfinders.co.uk

London Property Finders and Search Agents

I will leave the layout up to you, but a minimalist layout is preferred. If you would like to put additional detial or design on the card then that is up to, but not specified.

It is optional to have the company name on side 2, but if you do use it, please make it smaller. than on the 1st side.

The design needs to be simple, professional and not too in your face.

If you are using the black background design on side 1 for the logo, then maybe a white backgounnd can be used on side 2 with a black typeface.

The type face for the contacts details should be sans serif standard typeface. Please experiment with the desciprtion.

-

THE LETTERHEAD;

You can experiment with the layout for the letterhead. e.g logo centre aligned on the top of the page with the contact details and address at the bottom of the page OR the logo, description running along a bar on the top of the page with the contact details and website address at the bottom. Please try and experiment with this, but the less 'busy', the better.

Here is info that needs to be on the letterhead.

Bramwell Property Finders

t: 0208 394 2860

m: +44(0)7932 418 507

(PLEASE NOTE; the below company info must be placed at the bottom of the page as a footer, in small text.)

Kestrand Holdings Ltd Trading as Bramwell Property Finders, a company registered in England & Wales, No.7351926 , Registered office is 41 Hollinmoor Court, Hollinmoor Road, London, SW9 3PL, t: 0208 394 2860, m: +44(0)7932 418 507, e: info@bramwellpropertyfinders.co.uk

Best of luck!

Thank you

Dear Designer,

I have now attached the supporting files to this brief.

Thanks,

Owen Bramwell
Bramwell Property Finders

```html
<!DOCTYPE html>
<html lang="en">
<head>
<meta charset="utf-8">
<title>Bramwell Property Finders – Business Card</title>
<link rel="stylesheet" href="https://fonts.googleapis.com/css2?family=Source+Sans+3:wght@400&display=swap">
<style>
  :root {
    --stage: #f3f3f3;
    --ink: #1e1e1e;
    --black: #000000;
    --white: #ffffff;
    --accent: #7fb6de;
    --trim: #9a9a9a;
    --text-font: "Source Sans 3", "Myriad Pro", Arial, sans-serif;
  }
  html, body {
    margin: 0;
    padding: 0;
    width: 1200px;
    height: 348px;
    overflow: hidden;
    background: var(--stage);
  }
  .stage {
    position: relative;
    width: 1200px;
    height: 348px;
    font-family: var(--text-font);
  }

  /* Side 1 */
  .card-front {
    position: absolute;
    left: 13px;
    top: 19px;
    width: 581px;
    height: 300px;
    background: var(--black);
  }
  .card-front .brand-name {
    position: absolute;
    left: 0;
    right: 0;
    top: 152px;
    margin: 0;
    text-align: center;
    color: var(--white);
    font-weight: 400;
    font-size: 30px;
    letter-spacing: 2px;
    line-height: 1;
  }

  /* Side 2 */
  .card-back {
    position: absolute;
    left: 615px;
    top: 33px;
    width: 575px;
    height: 277px;
  }
  .card-back .trim-line {
    position: absolute;
    left: 7px;
    top: 0;
    width: 567px;
    height: 276px;
    border: 1px solid var(--trim);
    background: var(--white);
    box-sizing: border-box;
  }
  .card-back .top-band {
    position: absolute;
    left: 0;
    top: 13px;
    width: 569px;
    height: 31px;
    background: var(--black);
  }
  .card-back .brand-small {
    position: absolute;
    right: 42px;
    top: 0;
    height: 31px;
    line-height: 31px;
    margin: 0;
    color: var(--white);
    font-weight: 400;
    font-size: 13px;
    letter-spacing: 1px;
  }
  .card-back .contact-rule {
    position: absolute;
    left: 140px;
    top: 84px;
    width: 3px;
    height: 147px;
    background: var(--accent);
  }
  .card-back .contact-list {
    position: absolute;
    left: 153px;
    top: 84px;
    margin: 0;
    padding: 0;
    list-style: none;
    color: var(--ink);
    font-size: 20.5px;
    line-height: 29px;
  }
  .card-back .bottom-band {
    position: absolute;
    left: 0;
    top: 238px;
    width: 569px;
    height: 32px;
    background: var(--black);
  }
  .card-back .tagline {
    margin: 0;
    height: 32px;
    line-height: 32px;
    text-align: center;
    color: var(--accent);
    font-size: 20.5px;
    letter-spacing: 0.6px;
  }
</style>
</head>
<body>
  <main class="stage">
    <section class="card-front" aria-label="Business card, side 1">
      <p class="brand-name">BRAMWELL PROPERTY FINDERS</p>
    </section>

    <section class="card-back" aria-label="Business card, side 2">
      <div class="trim-line"></div>
      <div class="top-band">
        <p class="brand-small">BRAMWELL PROPERTY FINDERS</p>
      </div>
      <div class="contact-rule"></div>
      <ul class="contact-list">
        <li>Owen Bramwell</li>
        <li>t: 0208 394 2860</li>
        <li>m: +44(0)7932 418 507</li>
        <li>e: info@bramwellpropertyfinders.co.uk</li>
        <li>w: bramwellpropertyfinders.co.uk</li>
      </ul>
      <div class="bottom-band">
        <p class="tagline">London Property Finders and Search Agents</p>
      </div>
    </section>
  </main>
</body>
</html>
```